Design for Perch Lane real estate agency

Incorporate logo into new business cards. I need to include the Marlowe Ridge logo incorporated into Perch Lane on one side of the card (attached). On the other side I see just the icon with "Tessa Lorne" (attached) with "Rooted in Care" either included as is or removed from logo and rather put as a tag line on the business card separate from the main logo. Contact information:

Tessa Lorne
Associate Broker
Cell: 914-555-0173
Email: tessalorne@perchlane.example
Web: www.perchlane.example

Target Market(s)

Buyers, Sellers, Builders and Investors of homes and land

Industry/Entity Type

Real Estate Agent

Contact Information for Business Card

My client base tend to be higher end home buyers, sellers, builders and investors. I have been more and more in land and subdivisions for builders and investors. The card should not be cluttered. Clean and simple - yet with an air of exclusive/high end

Colors

Designer to choose colors to be used in the design.

Requirements
Must have
• Must have the logo on one side that has Marlowe Ridge logo incorporated. The side that has my contact information does not have to have the Marlowe Ridge logo incorporated.
• Must include "Rooted in Care" tag line either within logo (as is) or removed from logo and included in another position on the side of the business card with contact information.
Should not have
• Should not have Marlowe Ridge logo incorporated into Perch Lane logo on both sides of business card. Would like the Perch Lane logo that has Marlowe Logo only on the back side of card without contact information.

```html
<!DOCTYPE html>
<html lang="en">
<head>
<meta charset="utf-8">
<title>Perch Lane – Business Card</title>
<link href="https://fonts.googleapis.com/css2?family=EB+Garamond:wght@400;500&family=Cinzel:wght@500&family=Roboto:wght@400&family=Montserrat:wght@400&display=swap" rel="stylesheet">
<style>
  :root {
    --backdrop: #3a3a3a;
    --brown: #5e3f0c;
    --brown-light: #6c4b14;
    --gold: #c9a42b;
    --ink: #5a3c0c;
    --text: #3b2a10;
    --white: #ffffff;
  }
  * { margin: 0; padding: 0; box-sizing: border-box; }
  html, body {
    width: 1200px; height: 1000px; overflow: hidden;
    background: var(--backdrop);
  }
  .canvas { position: relative; width: 1200px; height: 1000px; }

  .card {
    position: absolute; left: 270px; width: 660px;
    box-shadow: 0 6px 18px rgba(0,0,0,.35);
  }

  /* Front side */
  .card--front {
    top: 108px; height: 377px;
    background: linear-gradient(135deg, var(--brown) 0%, var(--brown-light) 55%, var(--brown) 100%);
  }
  .front-texture { position: absolute; inset: 0; }
  .wordmark {
    position: absolute; left: 0; right: 0; top: 238px;
    text-align: center;
    font-family: "EB Garamond", serif; font-weight: 500;
    font-size: 56px; line-height: 1; color: var(--white);
    letter-spacing: -0.5px;
  }
  .wordmark-rule {
    position: absolute; left: 103px; top: 210px; width: 368px; height: 2px;
    background: var(--white);
  }
  .brokerage {
    position: absolute; left: 476px; top: 196px; width: 82px;
    text-align: center;
  }
  .brokerage-name {
    display: block; background: var(--white); color: var(--brown);
    font-family: "EB Garamond", serif; font-weight: 500;
    font-size: 11px; line-height: 26px; letter-spacing: .3px;
  }
  .brokerage-label {
    display: block; margin-top: 3px; color: var(--white);
    font-family: "EB Garamond", serif; font-size: 7px; letter-spacing: .2px;
    white-space: nowrap;
  }

  /* Back side */
  .card--back {
    top: 520px; height: 380px; background: var(--white);
  }
  .emblem {
    position: absolute; left: 294px; top: 60px; width: 72px; height: 72px;
    border-radius: 50%; background: var(--gold);
  }
  .agent-name {
    position: absolute; left: 0; right: 0; top: 142px; text-align: center;
    font-family: "Cinzel", serif; font-weight: 500; font-size: 30px;
    letter-spacing: 3px; color: var(--ink);
  }
  .agent-title {
    position: absolute; left: 0; right: 0; top: 178px;
    display: flex; justify-content: center; align-items: center; gap: 8px;
    font-family: "Roboto", sans-serif; font-size: 14px; color: var(--gold);
  }
  .agent-title::before, .agent-title::after {
    content: ""; width: 48px; height: 1px; background: var(--ink);
  }
  .contact {
    position: absolute; left: 0; right: 0; top: 218px;
    font-family: "Roboto", sans-serif; font-size: 14px; color: var(--text);
    text-align: center;
  }
  .contact-row { display: flex; justify-content: center; align-items: center; gap: 10px; }
  .contact-item { display: inline-flex; align-items: center; gap: 5px; }
  .contact-item svg { width: 11px; height: 11px; }
  .website { margin-top: 6px; }
  .website .accent { color: var(--gold); }
  .tagline-band {
    position: absolute; left: 0; right: 0; top: 318px; height: 40px;
    border-top: 2px solid var(--gold); border-bottom: 2px solid var(--gold);
    background: var(--brown);
    display: flex; align-items: center; justify-content: center;
    font-family: "Montserrat", sans-serif; font-size: 13px;
    letter-spacing: 5px; color: var(--white); text-transform: uppercase;
  }
</style>
</head>
<body>
<main class="canvas">
  <section class="card card--front">
    <div class="front-texture" role="img" aria-label="Faint repeating pattern of the house emblem across the brown background"></div>
    <h1 class="wordmark">Perch Lane</h1>
    <div class="wordmark-rule"></div>
    <div class="brokerage">
      <span class="brokerage-name">MARLOWE RIDGE</span>
      <span class="brokerage-label">RESIDENTIAL BROKERAGE</span>
    </div>
  </section>

  <section class="card card--back">
    <div class="emblem" aria-hidden="true"></div>
    <h2 class="agent-name">TESSA LORNE</h2>
    <p class="agent-title">Associate Broker</p>
    <div class="contact">
      <div class="contact-row">
        <span class="contact-item">
          <svg viewBox="0 0 12 12" aria-hidden="true"><path d="M3 1 L5 3.5 L4 5 Q5 7.5 7 8 L8.5 7 L11 9 L9.5 11 Q3.5 10.5 1 3 Z" fill="#c9a42b"/></svg>
          914-555-0173
        </span>
        <span class="contact-item">
          <svg viewBox="0 0 12 12" aria-hidden="true"><rect x="1" y="2.5" width="10" height="7" fill="#c9a42b"/><path d="M1 2.5 L6 6.5 L11 2.5" stroke="#fff" stroke-width="1" fill="none"/></svg>
          tessalorne@perchlane.example
        </span>
      </div>
      <p class="website">www.<span class="accent">perchlane</span>.example</p>
    </div>
    <div class="tagline-band">Rooted in Care</div>
  </section>
</main>
</body>
</html>
```